Direct to Consumer extended service contract business with a new disruptive business model needs a

We need a customized wordpress design for a company called 'Tall Harbor Assurance'.
We provide an innovative and unique service contract protection program direct to consumers. This program provides monthly coverage for all electronics purchased in the last 4 years and all electronics the consumer purchases in the future for a low monthly fee. The overall design should communicate a sense of legitimacy, ethics, and superior customer service and support (in an industry that has a huge PR issue to overcome).
Electronics is the first product group, other product groups with different price points to launch in the future..

Target Market(s)

All purchasers of electronic goods...all demographics

Industry/Entity Type

Electronics

Font styles to use
Sans Serif

Requirements
Must have
• Customer Testimonials
Industry News
Customer ratings
Blog posts
Call to action messaging
Like the functional elements and design of bramblequill.example (need to be better)
Nice to have
• Like to see video testimonials
Social network "whats trending related to electronics or service contract industry"
Easy way to register products for warranty

```html
<!DOCTYPE html>
<html lang="en">
<head>
<meta charset="utf-8">
<title>Tall Harbor Assurance</title>
<link rel="stylesheet" href="https://fonts.googleapis.com/css2?family=Hind:wght@300;400;500;600;700&display=swap">
<style>
:root{
  --navy:#22364f;
  --navy-dark:#1b2c41;
  --ink:#1d1d1d;
  --text:#555;
  --muted:#9a9a9a;
  --blue:#1e7fd8;
  --blue-badge:#3f9be8;
  --red:#e2412f;
  --gold:#f0c419;
  --star-off:#d4d4d4;
  --news-bg:#ebebeb;
  --cta-bg:#e4e4e4;
  --blog-bg:#d3e5f6;
  --chirp:#5eabd8;
  --orbit:#e0513a;
  --panel-gray:#efefef;
  --white:#fff;
}
*{box-sizing:border-box;margin:0;padding:0}
html,body{width:1200px;height:3683px;overflow:hidden}
body{font-family:"Hind",Arial,sans-serif;color:var(--text);background:var(--white);font-size:14px;line-height:1.4}
a{color:inherit;text-decoration:none}
.container{width:876px;margin:0 auto;position:relative;height:100%}
.section-title{font-size:22px;font-weight:700;color:var(--ink);letter-spacing:-.2px}
.stars{color:var(--gold);letter-spacing:2px;font-size:15px}
.stars .off{color:var(--star-off)}
.link-blue{color:var(--blue)}
.link-red{color:var(--red)}

/* Header */
.site-header{height:92px;background:var(--navy);position:relative;z-index:2}
.brand{position:absolute;left:0;top:0;height:86px;width:96px;background:var(--navy-dark);display:flex;flex-direction:column;align-items:center;justify-content:center;gap:6px;color:#e9dcc0}
.brand-square{width:26px;height:26px;border:2px solid #e9dcc0}
.brand-name{font-size:9px;font-weight:600;text-align:center;line-height:1.1;letter-spacing:.5px}
.utility{position:absolute;right:0;top:8px;display:flex;gap:22px;font-size:11px;color:#c9d2de}
.main-nav{position:absolute;right:0;top:48px;display:flex;gap:38px;font-size:14px;color:var(--white);font-weight:500}
.main-nav .active{border-bottom:2px solid var(--white);padding-bottom:4px}

/* Hero */
.hero{height:414px;background:#f7f7f7;position:relative;overflow:hidden}
.hero-photo{position:absolute;left:668px;top:0;width:532px;height:414px;background:linear-gradient(160deg,#3a3d42 0%,#17181b 45%,#6b4a1c 75%,#d7a43a 100%)}
.hero-copy{position:absolute;left:169px;top:50px;width:520px}
.hero-title{font-size:46px;line-height:1.1;font-weight:500;color:var(--ink);letter-spacing:-.8px}
.hero-title em{font-style:normal;color:var(--red);font-weight:700}
.hero-text{margin-top:26px;font-size:19px;line-height:1.45;color:#555;font-weight:300;width:480px}
.hero-register{display:block;margin-top:24px;font-size:21px;color:var(--red);font-weight:500}
.save-badge{position:absolute;left:705px;top:36px;width:140px;height:140px;border-radius:50%;background:var(--blue-badge);color:var(--white);display:flex;flex-direction:column;align-items:center;justify-content:center;line-height:1;font-weight:600}
.save-badge span{font-size:30px}
.save-badge strong{font-size:40px;font-weight:700}

/* CTA */
.cta-bar{height:47px;background:var(--cta-bg);display:flex;align-items:center;justify-content:center;font-size:22px;font-weight:600;color:var(--navy);letter-spacing:.3px;border-bottom:1px solid #d6d6d6}
.cta-bar a{color:var(--blue);margin-left:8px}

/* News */
.news{height:552px;background:var(--news-bg)}
.news .section-title{position:absolute;top:52px;left:0}
.more{position:absolute;right:0;font-size:22px;color:#b4b4b4;font-weight:400}
.news .more{top:50px}
.news-grid{position:absolute;top:110px;left:0;right:0;display:grid;grid-template-columns:1fr 1fr;column-gap:40px;row-gap:28px}
.news-item{display:flex;gap:14px}
.news-thumb{flex:0 0 66px;height:56px;background:linear-gradient(135deg,#6d7a86,#2f3a45)}
.news-thumb.warm{background:linear-gradient(135deg,#a58a6a,#4b3a2c)}
.news-item h3{font-size:15px;line-height:1.25;color:var(--ink);font-weight:600}
.news-item p{font-size:12.5px;line-height:1.35;color:#666;margin-top:4px}

/* Testimonials */
.testimonials{height:675px}
.testimonials .section-title{position:absolute;top:68px}
.video-row{position:absolute;top:127px;left:0;right:0;display:grid;grid-template-columns:repeat(3,1fr);gap:24px}
.video-thumb{height:146px;position:relative;background:linear-gradient(135deg,#5b4d43,#1e1a18)}
.video-thumb.cool{background:linear-gradient(135deg,#4d5a66,#15191d)}
.video-thumb.mid{background:linear-gradient(135deg,#6a5a4a,#2a2420)}
.video-thumb svg{position:absolute;left:50%;top:50%;transform:translate(-50%,-50%)}
.video-quote{margin-top:16px;font-size:15px;line-height:1.25;color:var(--ink);font-weight:600}
.byline{display:flex;justify-content:space-between;align-items:center;margin-top:8px;font-size:11.5px;color:#777}
.quote-divider{position:absolute;top:440px;left:0;right:0;border-top:1px solid #e3e3e3}
.quote-row{position:absolute;top:462px;left:0;right:0;display:grid;grid-template-columns:repeat(3,1fr);gap:24px}
.quote-row blockquote{font-size:13px;line-height:1.35;color:#444}
.quote-row .byline{margin-top:8px;justify-content:flex-start;gap:16px}

/* Blog */
.blog{height:544px;background:var(--blog-bg)}
.blog .section-title{position:absolute;top:44px}
.blog .more{top:42px;color:#5a6a7c}
.blog-grid{position:absolute;top:103px;left:0;right:0;display:grid;grid-template-columns:repeat(3,1fr);gap:24px}
.blog-card{background:var(--white);height:372px;position:relative}
.blog-photo{height:146px;background:linear-gradient(135deg,#3d3530,#a0532e)}
.blog-photo.phone{background:linear-gradient(135deg,#d8d2c6,#8a8276)}
.blog-photo.stage{background:linear-gradient(135deg,#6c6f78,#1f2228)}
.blog-body{padding:16px 18px}
.blog-body h3{font-size:21px;line-height:1.15;color:var(--ink);font-weight:500}
.blog-body p{font-size:12.5px;line-height:1.35;color:#666;margin-top:10px}
.blog-foot{position:absolute;left:18px;right:18px;bottom:16px;display:flex;justify-content:space-between;font-size:12px;color:var(--ink)}
.blog-foot .comments b{color:var(--red);font-weight:500}

/* Customers */
.customers{height:440px}
.customers .section-title{position:absolute;top:50px}
.customer-grid{position:absolute;top:118px;left:0;right:0;display:grid;grid-template-columns:repeat(4,1fr);text-align:center}
.customer-name{height:60px;display:flex;align-items:center;justify-content:center;font-size:26px;font-weight:600;color:var(--navy)}
.customer-grid .stars{display:block;margin-top:18px;font-size:20px}
.customer-grid h4{font-size:13px;font-weight:700;color:var(--ink);margin-top:10px}
.customer-grid p{font-size:12px;color:#666}
.customer-grid a{font-size:12px;color:var(--red)}

/* Social */
.social{height:490px}
.social .section-title{position:absolute;top:24px}
.social-panels{position:absolute;top:61px;left:0;right:0;height:429px;display:grid;grid-template-columns:repeat(3,1fr)}
.panel{padding:22px 20px;position:relative;font-size:12px}
.panel-head{display:flex;gap:10px;align-items:flex-start;line-height:1.25}
.panel-icon{width:26px;height:26px;flex:0 0 26px}
.panel-circle{background:var(--panel-gray)}
.panel-circle .panel-head{color:var(--ink);font-weight:600}
.panel-photo{margin-top:18px;height:190px;background:linear-gradient(135deg,#9c9892,#5c5954)}
.panel-circle p{margin-top:16px;color:#555;font-size:12.5px;line-height:1.35}
.panel-chirp{background:var(--chirp);color:var(--white)}
.panel-chirp .panel-icon,.panel-orbit .panel-icon{background:rgba(255,255,255,.9);margin-left:auto}
.panel-orbit{background:var(--orbit);color:var(--white)}
.panel-big{margin-top:28px;font-size:22px;line-height:1.2;font-weight:500}
.panel-date{margin-top:18px;font-size:11px;opacity:.9}

/* Footer */
.site-footer{height:338px;background:var(--navy);color:#dfe5ec}
.footer-grid{position:absolute;top:54px;left:0;right:0;display:grid;grid-template-columns:repeat(4,1fr);gap:24px;font-size:12px;line-height:1.45}
.footer-grid h5{font-size:12.5px;font-weight:600;color:var(--white);margin-bottom:12px}
.footer-grid li{list-style:none}
.social-squares{display:grid;grid-template-columns:repeat(5,20px);gap:6px;margin-top:12px}
.social-squares i{display:block;width:20px;height:20px;background:#4f7fbf}
.social-squares i:nth-child(3n){background:#5eabd8}
.social-squares i:nth-child(4n){background:#d9513f}
.copyright{height:91px;display:flex;align-items:center;justify-content:center;font-size:11.5px;color:#555;background:#f3f3f3}
.copyright b{color:var(--ink)}
</style>
</head>
<body>

<header class="site-header">
  <div class="container">
    <a class="brand" href="#"><span class="brand-square"></span><span class="brand-name">TALL HARBOR<br>ASSURANCE</span></a>
    <div class="utility"><span>Log in</span><span>Support</span><span>1-800-555-0142</span></div>
    <nav class="main-nav">
      <a href="#">Home</a><a class="active" href="#">About us</a><a href="#">Warranty</a><a href="#">Electronic devices</a><a href="#">Service</a><a href="#">Contact</a>
    </nav>
  </div>
</header>

<section class="hero">
  <div class="hero-photo" role="img" aria-label="Close-up of a smartphone showing a bright flower on its screen"></div>
  <div class="save-badge"><span>save</span><strong>60%</strong></div>
  <div class="hero-copy">
    <h1 class="hero-title">Save up to <em>60%</em> vs. your current electronic insurance.</h1>
    <p class="hero-text">Enjoy the personal attention you deserve. A Northfield agent is ready to help you with all your insurance needs. Find yours today.</p>
    <a class="hero-register" href="#">→ Register your electronic product now.</a>
  </div>
</section>

<div class="cta-bar">GET A QUOTE TODAY <a href="#">CLICK HERE</a></div>

<section class="news">
  <div class="container">
    <h2 class="section-title">The latest news.</h2>
    <a class="more" href="#">More news items</a>
    <div class="news-grid">
      <article class="news-item"><div class="news-thumb" role="img" aria-label="News photo"></div><div><h3>Per 6 januari 2014 verdwijnt het sofinummer</h3><p>Per 6 januari 2014 verdwijnt het sofinummer. Vanaf dat moment kan alleen een Persoonlijk Nummer worden gebruikt. <a class="link-blue" href="#">Lees meer.</a></p></div></article>
      <article class="news-item"><div class="news-thumb warm" role="img" aria-label="Portrait photo for news item"></div><div><h3>Per 6 januari 2014 verdwijnt het sofinummer</h3><p>Per 6 januari 2014 verdwijnt het sofinummer. Vanaf dat moment kan alleen een Persoonlijk Nummer worden gebruikt. <a class="link-blue" href="#">Lees meer.</a></p></div></article>
      <article class="news-item"><div class="news-thumb" role="img" aria-label="News photo"></div><div><h3>Ook na 1 maart 2014 verlaagde BTW op renovatie en onderhoud</h3><p>De verlaagde BTW tarief van 6% voor renovatie en onderhoud was geldig tot 1 maart 2014. <a class="link-blue" href="#">Lees meer.</a></p></div></article>
      <article class="news-item"><div class="news-thumb warm" role="img" aria-label="Portrait photo for news item"></div><div><h3>Ook na 1 maart 2014 verlaagde BTW op renovatie en onderhoud</h3><p>De verlaagde BTW tarief van 6% voor renovatie en onderhoud was geldig tot 1 maart 2014. <a class="link-blue" href="#">Lees meer.</a></p></div></article>
      <article class="news-item"><div class="news-thumb warm" role="img" aria-label="News photo"></div><div><h3>2014: Verlaging van box 2 tarief van 25% naar 22%</h3><p>De Fiscale Dienst controleert dit najaar extra op openstaande lege schulden over de jaren 2008-2012. De Fiscale Dienst vergelijkt het aangifte schuld heeft, zult u een <a class="link-blue" href="#">Lees meer.</a></p></div></article>
      <article class="news-item"><div class="news-thumb" role="img" aria-label="Portrait photo for news item"></div><div><h3>per 2014: Verlaging van box 2 tarief van 25% naar 22%</h3><p>De Fiscale Dienst controleert dit najaar extra op openstaande lege schulden over de jaren 2008-2012. De Fiscale Dienst vergelijkt het aangifte schuld belastingverklaring van uw BV. <a class="link-blue" href="#">Lees meer.</a></p></div></article>
    </div>
  </div>
</section>

<section class="testimonials">
  <div class="container">
    <h2 class="section-title">Testimonials.</h2>
    <div class="video-row">
      <article>
        <div class="video-thumb" role="img" aria-label="Video still of a customer speaking"><svg width="46" height="46" viewBox="0 0 46 46"><circle cx="23" cy="23" r="20" fill="none" stroke="#3f9be8" stroke-width="3"/><path d="M18 14l13 9-13 9z" fill="#3f9be8"/></svg></div>
        <p class="video-quote">No matter where you live, Northfield renters insurance can help you stay protected.</p>
        <div class="byline"><span>– Dale Rinner</span><span class="stars">★★★<span class="off">★★</span></span></div>
      </article>
      <article>
        <div class="video-thumb cool" role="img" aria-label="Video still of a customer speaking"><svg width="46" height="46" viewBox="0 0 46 46"><circle cx="23" cy="23" r="20" fill="none" stroke="#3f9be8" stroke-width="3"/><path d="M18 14l13 9-13 9z" fill="#3f9be8"/></svg></div>
        <p class="video-quote">only best customer service! Pulse 5 battery reimbursed 100% without fight.</p>
        <div class="byline"><span>– Owen Marsh</span><span class="stars">★★★<span class="off">★★</span></span></div>
      </article>
      <article>
        <div class="video-thumb mid" role="img" aria-label="Video still of a customer speaking"><svg width="46" height="46" viewBox="0 0 46 46"><circle cx="23" cy="23" r="20" fill="none" stroke="#3f9be8" stroke-width="3"/><path d="M18 14l13 9-13 9z" fill="#3f9be8"/></svg></div>
        <p class="video-quote">Got my check today for my #P5! Guaranteed buyback paid me to upgrade my phone! #goodagain</p>
        <div class="byline"><span>– Owen Marsh</span><span class="stars">★★★<span class="off">★★</span></span></div>
      </article>
    </div>
    <div class="quote-divider"></div>
    <div class="quote-row">
      <div><blockquote>"Nothing is impossible, the word itself says 'I'm possible'!"</blockquote><div class="byline"><span>– Clara Voss</span></div><span class="stars">★★★<span class="off">★★</span></span></div>
      <div><blockquote>"The best and most beautiful things in the world cannot be seen or even touched – they must be felt with the heart."</blockquote><div class="byline"><span>– Ida Brenn</span><span class="stars">★★★<span class="off">★★</span></span></div></div>
      <div><blockquote>"As we express our gratitude, we must never forget that the highest appreciation is not to utter words, but to live by them."</blockquote><div class="byline"><span>– Rafe Olin</span><span class="stars">★★★<span class="off">★★</span></span></div></div>
    </div>
  </div>
</section>

<section class="blog">
  <div class="container">
    <h2 class="section-title">The latest blog stories.</h2>
    <a class="more" href="#">More blog items</a>
    <div class="blog-grid">
      <article class="blog-card">
        <div class="blog-photo" role="img" aria-label="Speaker on a stage presenting a wearable device"></div>
        <div class="blog-body"><h3>Halvern senior execs resign ahead of smart wearable launch.</h3><p>Halvern has its back on its road to recovery thanks to its Aria X8 flagship phone but it's now facing yet another.</p></div>
        <div class="blog-foot"><a href="#">Read more</a><span class="comments"><b>21</b> Comments</span></div>
      </article>
      <article class="blog-card">
        <div class="blog-photo phone" role="img" aria-label="Smartphone lying on a table showing its lock screen"></div>
        <div class="blog-body"><h3>Daily Ledger writer gives Chirper password to the internet and the obs.</h3><p>We put a ton of trust in technology of your password? Cole Amsel of The Daily Ledger is in.</p></div>
        <div class="blog-foot"><a href="#">Read more</a><span class="comments"><b>76</b> Comments</span></div>
      </article>
      <article class="blog-card">
        <div class="blog-photo stage" role="img" aria-label="People gathered around a large curved television"></div>
        <div class="blog-body"><h3>Lumora has a very flexible 18-inch display, promises 60-inch TVs.</h3><p>It's been a while since we've seen any new curved or flexible displays following Lumora and Solmira's display.</p></div>
        <div class="blog-foot"><a href="#">Read more</a><span class="comments"><b>5</b> Comments</span></div>
      </article>
    </div>
  </div>
</section>

<section class="customers">
  <div class="container">
    <h2 class="section-title">Our biggest customers.</h2>
    <div class="customer-grid">
      <div><div class="customer-name">Quartzline</div><span class="stars">★★★<span class="off">★★</span></span><h4>Quartzline laptops &amp; computers</h4><p>4.5 average on 7000+ reviews</p><a href="#">Read the reviews</a></div>
      <div><div class="customer-name">Veyra</div><span class="stars">★★★<span class="off">★★</span></span><h4>Veyra hardware store</h4><p>4.5 average on 7000+ reviews</p><a href="#">Read the reviews</a></div>
      <div><div class="customer-name">Solmira</div><span class="stars">★★★<span class="off">★★</span></span><h4>Solmira Mobile Worldwide</h4><p>4.5 average on 7000+ reviews</p><a href="#">Read the reviews</a></div>
      <div><div class="customer-name">Droidwell</div><span class="stars">★★★<span class="off">★★</span></span><h4>Droidwell Mobile</h4><p>4.5 average on 7000+ reviews</p><a href="#">Read the reviews</a></div>
    </div>
  </div>
</section>

<section class="social">
  <div class="container">
    <h2 class="section-title">Lets become friends on socialmedia.</h2>
    <div class="social-panels">
      <div class="panel panel-circle">
        <div class="panel-head"><span>Latest on Circlebook<br><span class="link-blue">circlebook.example/tallharbor</span></span></div>
        <div class="panel-photo" role="img" aria-label="Company emblem stitched on fabric"></div>
        <p>"De voorsvage regimes van 4000 stickers ontworpen stickers 4.8 afdeling van de club, bij het evenement in Rotterdam"</p>
      </div>
      <div class="panel panel-chirp">
        <div class="panel-head"><span>Latest on Chirper<br>@tallharbor</span><span class="panel-icon"></span></div>
        <p class="panel-big">Leuk! CD competitie begint dit weekend. BAC doet mee met 15 teams, veel plezier allemaal (én bedankt @Baanclub)</p>
        <p class="panel-date">12:30 – Donderdag 8 Mei 2014</p>
      </div>
      <div class="panel panel-orbit">
        <div class="panel-head"><span>Laatste van Orbitly<br>orbitly.example/tallharbor</span><span class="panel-icon"></span></div>
        <p class="panel-big">350 deelnemers bij de BAC indoor clubkampioenschappen! Het is een feestje!</p>
        <p class="panel-date">14:45 – Maandag 5 Mei 2014</p>
      </div>
    </div>
  </div>
</section>

<footer class="site-footer">
  <div class="container">
    <div class="footer-grid">
      <div><h5>Warranty plans</h5><ul><li>Phone Warranty</li><li>Nova Warranty</li><li>Halvern One Warranty</li><li>Nexa Warranty</li><li>Strider Warranty</li><li>Other Smartphone</li><li>Cloudbook Warranty</li><li>Delmar Laptop Warranty</li><li>Other Warranty's</li></ul></div>
      <div><h5>Menu</h5><ul><li>My Profile</li><li>Register Plan</li><li>Claims Center</li><li>Our Coverage</li><li>Tech Support</li><li>Legal Notices</li><li>FAQs &amp; Support</li><li>How-To Videos</li><li>Privacy Policy</li></ul></div>
      <div><h5>Socialmedia</h5><p>Volg ons via social media</p><div class="social-squares"><i></i><i></i><i></i><i></i><i></i><i></i><i></i><i></i><i></i><i></i></div></div>
      <div><h5>Latest news story</h5><p>Ron's Weigh I Passed Out! sipurkyout working towards Each choice is a step toward Permission to Accept Yourself In celebration of Ciscar de I have a product review the Enough for two stuffed tight Fit: A Fifty-Something's</p></div>
    </div>
  </div>
</footer>

<div class="copyright"><span>Copyright © 2014 <b>Tall Harbor Assurance</b>. Use of this website constitutes acceptance of our <b>User Agreement</b> and <b>Privacy Policy</b>.</span></div>

</body>
</html>
```